Lumo Voyages
business cards & letterhead
Lumo Voyages -
Creative Brief
Bright & Fun-filled
Corinne Maddox
58214 Birchwood Ln Rockville, MD 20817
lumovoyages@quellnet.example

```html
<!DOCTYPE html>
<html lang="en">
<head>
<meta charset="utf-8">
<title>Lumo Voyages – Business Card</title>
<link rel="stylesheet" href="https://fonts.googleapis.com/css2?family=Arimo:wght@400;700&display=swap">
<style>
  :root {
    --backdrop: #e9e7e3;
    --card: #ffffff;
    --brand-blue: #1b76bc;
    --wave-blue: #1a86c8;
    --wave-blue-light: #5db4e5;
    --wave-green: #8cc63f;
    --wave-green-light: #c4e08a;
    --text-grey: #4d4d4d;
    --divider: #b8b8b8;
  }
  * { margin: 0; padding: 0; box-sizing: border-box; }
  html, body {
    width: 1200px; height: 780px; overflow: hidden;
    background: var(--backdrop);
    font-family: "Arimo", Arial, sans-serif;
  }
  .business-card {
    position: absolute; left: 40px; top: 40px;
    width: 1120px; height: 700px;
    background: var(--card);
    border-radius: 44px;
    overflow: hidden;
    box-shadow: 0 6px 24px rgba(0,0,0,0.12);
  }
  .brand {
    position: absolute; top: 190px; left: 0; width: 100%;
    display: flex; align-items: center; justify-content: center; gap: 26px;
  }
  .brand-dot {
    width: 92px; height: 92px; border-radius: 50%;
    background: var(--wave-blue);
  }
  .brand-name {
    font-size: 74px; font-weight: 700; color: var(--brand-blue);
    letter-spacing: 1px;
  }
  .holder-name {
    position: absolute; top: 365px; left: 0; width: 100%;
    text-align: center;
    font-size: 38px; font-weight: 700; color: var(--brand-blue);
  }
  .contact {
    position: absolute; top: 440px; left: 0; width: 100%;
    display: flex; justify-content: center;
    color: var(--text-grey); font-size: 24px; line-height: 1.55;
  }
  .contact-address { text-align: right; padding-right: 30px; padding-top: 22px; }
  .contact-divider { width: 2px; background: var(--divider); height: 112px; }
  .contact-lines { padding-left: 26px; }
  .contact-line { display: flex; align-items: center; gap: 12px; }
  .contact-line.email { font-size: 20px; }
  .contact-icon { width: 24px; height: 24px; flex: none; }
  .card-waves { position: absolute; left: 0; bottom: 0; width: 1120px; height: 700px; }
</style>
</head>
<body>
  <div class="business-card">
    <svg class="card-waves" viewBox="0 0 1120 700" aria-hidden="true">
      <path d="M0 575 C 260 640, 600 640, 1120 540 L1120 565 C 620 665, 260 665, 0 610 Z" fill="var(--wave-green-light)"/>
      <path d="M0 565 C 280 625, 640 625, 1120 515 L1120 545 C 640 640, 270 650, 0 600 Z" fill="var(--wave-green)"/>
      <path d="M0 615 C 300 680, 680 660, 1120 575 L1120 700 L0 700 Z" fill="var(--wave-blue-light)"/>
      <path d="M0 635 C 320 700, 700 675, 1120 595 L1120 700 L0 700 Z" fill="var(--wave-blue)"/>
    </svg>

    <div class="brand">
      <span class="brand-dot"></span>
      <span class="brand-name">Lumo Voyages</span>
    </div>

    <div class="holder-name">Corinne Maddox</div>

    <div class="contact">
      <div class="contact-address">
        58214 Birchwood Ln<br>
        Rockville, MD 20817
      </div>
      <div class="contact-divider"></div>
      <div class="contact-lines">
        <div class="contact-line phone">
          <svg class="contact-icon" viewBox="0 0 24 24" aria-hidden="true">
            <path d="M6.6 3.5 L9.3 6.5 L7.6 9 C8.6 11.4 10.6 13.6 13.1 14.8 L15.6 13 L18.6 15.8 L16.8 19.4 C10.3 19 4.8 13.4 4.5 6.3 Z" fill="var(--wave-blue)"/>
          </svg>
          <span>301-555-0142</span>
        </div>
        <div class="contact-line email">
          <svg class="contact-icon" viewBox="0 0 24 24" aria-hidden="true">
            <circle cx="12" cy="12" r="4" fill="none" stroke="var(--wave-blue)" stroke-width="2.4"/>
            <path d="M16 8 V14 C16 16.5 20 16.5 20 12 A8 8 0 1 0 15.5 19.2" fill="none" stroke="var(--wave-blue)" stroke-width="2.4" stroke-linecap="round"/>
          </svg>
          <span>lumovoyages@quellnet.example</span>
        </div>
      </div>
    </div>
  </div>
</body>
</html>
```